Internal Office Slogans / Motto / Vision Statements

Hi. We would like to put up some posters around the office with quotations such as -
-”Do what you do so well that they will want to see it again and bring their friends.”- Harlan Pruett
-Make your customers feel heard and understood. Make your customers feel respected and liked. Make your customers feel appreciated and helped. Understand that you can do none of these things unless you are sincere about them.
Gordon Felsk
- It’s a very predictable and satisfying phenomenon: whenever we get better, our customers do too.
Ray Tolbin
-Catch people in the act of performing extraordinary customer service. Treat them like heroes. Tell their stories, far and wide.
Neil Hartcombe

The purpose of the posters is to reiterate our culture and vision within the organisation. They should be clean, crisp and eye catching, not gaudy or bright. Professional, bold and strong.

The company website and logo is at http://www.norvanta.com.au
Print size will be A1

Thanks for participating & looking forward to seeing your great work.
Updates

Hi All. . 

So to reiterate we are looking for one background design to be used for multiple quotes...  The list of quotes are as follows: 

Support and or Sales Office

 

Make your customers feel heard and understood.Make your customers feel respected and liked. Make your customers feelappreciated and helped. Understand that you can do none of these things unlessyou are sincere about them.

Gordon Felsk

 

Nothing liberates our greatness like the desireto help, the desire to serve

Rosalind Pevrell

 

It’s a very predictable and satisfying phenomenon:whenever we get better, our customers do too.

Ray Tolbin

 

Success means we go to sleep at night knowingthat our talents and abilities were used in a way that served others.

Rosalind Pevrell.

 

The sole purpose of business is to create, serveand satisfy a customer, from beginning to end – and that’s everyone’s job.

Neil Hartcombe

 

We don’t celebrate closing a sale, we celebrateopening a relationship.

Eleanor Quisk

I will never make you a promise – unless I giveyou a plan and procedure to make that promise possible.

Lon Borstad

 

Customers feel we take them for granted; onlyshow interest when we want an order; lavish our time on prospects; communicatemainly by invoice; are fixated on big accounts; drop them like hot potatoesonce we have the order; don’t follow through on promises; and satisfy our ownbureaucracy rather than their needs. We can do better than that, much better.

Peter K Almsby.

 

 

General and public area

 

Catch people in the act of performingextraordinary customer service. Treat them like heroes. Tell their stories, farand wide.

Neil Hartcombe

 

 

We see our customers as invited guests to aparty, and we are the hosts. It’s our job every day to make every importantaspect of the customer experience a little bit better." Carl Dunmore - Founder andCEO of Veltrona

 

"If you do build a great experience,customers tell each other about that. Word of mouth is verypowerful."  Carl Dunmore

 

It's not a faithin technology. It's faith in people. Frank Toller

 

“Being the richest man in the cemetery doesn’tmatter to me … Going to bed at night saying we’ve done something wonderful…that’s what matters to me.” Frank Toller

 

The customer experience is the next competitivebattleground. Terry Mandevic, CIO, Quorra Computers

 

”Do what you do so well that they will want tosee it again and bring their friends.”- Harlan Pruett

In the world of internet customer service, it isimportant to remember your competitor is only a mouse click away. GlennPirsley (not sure who he is but like the quote).

The customer is why you go to work. If they goaway, you do, too. Simon Largotti (?)

 

MaybeSome for Sales or Build Team:

Quality is remembered long after the price is forgotten. Renzoli Family Slogan

```html
<!DOCTYPE html>
<html lang="en">
<head>
<meta charset="utf-8">
<title>Hero Stories Poster</title>
<link rel="stylesheet" href="https://fonts.googleapis.com/css2?family=Questrial&family=Montserrat:wght@700;800&family=Jura:wght@600&display=swap">
<style>
  :root {
    --ink-white: #ffffff;
    --attribution-tan: #e9b27b;
    --night-black: #0a0908;
    --night-deep: #15110f;
    --glow-warm: #4a3a2c;
    --divider-grey: #6c6a68;
  }
  html, body {
    margin: 0;
    padding: 0;
    width: 849px;
    height: 1200px;
    overflow: hidden;
    background: var(--night-black);
  }
  .poster {
    position: relative;
    width: 849px;
    height: 1200px;
    overflow: hidden;
  }
  .bokeh-backdrop {
    position: absolute;
    inset: 0;
    background:
      linear-gradient(180deg,
        var(--night-deep) 0%,
        var(--night-black) 35%,
        var(--night-black) 60%,
        var(--glow-warm) 78%,
        var(--night-deep) 92%,
        var(--night-black) 100%);
  }
  .quote {
    position: absolute;
    inset: 0;
    margin: 0;
    color: var(--ink-white);
    text-align: center;
    text-transform: uppercase;
  }
  .quote-line {
    position: absolute;
    left: 0;
    right: 0;
    line-height: 1;
    white-space: nowrap;
    font-family: "Questrial", sans-serif;
    letter-spacing: 1px;
  }
  .quote-line strong,
  .quote-line.is-bold {
    font-family: "Montserrat", sans-serif;
    font-weight: 800;
  }
  .line-1 { top: 58px;  font-size: 60px; }
  .line-2 { top: 158px; font-size: 60px; }
  .line-3 { top: 256px; font-size: 60px; }
  .line-4 { top: 355px; font-size: 58px; letter-spacing: 3px; }
  .line-5 { top: 455px; font-size: 62px; letter-spacing: 3px; }
  .line-6 { top: 550px; font-size: 82px; letter-spacing: 3px; }
  .line-7 { top: 665px; font-size: 58px; }
  .line-8 { top: 757px; font-size: 86px; letter-spacing: 3px; }
  .line-9 { top: 864px; font-size: 54px; }
  .line-10 { top: 946px; font-size: 48px; font-weight: 700; }
  .line-9 strong { font-weight: 700; }
  .divider {
    position: absolute;
    left: 0;
    top: 1025px;
    width: 849px;
    height: 4px;
  }
  .attribution {
    position: absolute;
    left: 0;
    right: 0;
    top: 1060px;
    margin: 0;
    text-align: center;
    font-family: "Jura", sans-serif;
    font-weight: 600;
    font-size: 56px;
    line-height: 1;
    letter-spacing: 2px;
    text-transform: uppercase;
    color: var(--attribution-tan);
  }
</style>
</head>
<body>
  <main class="poster">
    <div class="bokeh-backdrop" role="img" aria-label="Blurred night city lights with soft warm and teal bokeh circles on black"></div>

    <blockquote class="quote">
      <div class="quote-line line-1">Catch people</div>
      <div class="quote-line line-2">In the <strong>act</strong> of</div>
      <div class="quote-line line-3">Performing</div>
      <div class="quote-line line-4 is-bold">Extraordinary</div>
      <div class="quote-line line-5 is-bold">Customer</div>
      <div class="quote-line line-6 is-bold">Service.</div>
      <div class="quote-line line-7">Treat them like</div>
      <div class="quote-line line-8 is-bold">Heroes.</div>
      <div class="quote-line line-9">Tell their <strong>stories.</strong></div>
      <div class="quote-line line-10 is-bold">Far and wide.</div>
    </blockquote>

    <svg class="divider" viewBox="0 0 849 4" aria-hidden="true">
      <line x1="0" y1="2" x2="849" y2="2" stroke="var(--divider-grey)" stroke-width="4" stroke-dasharray="6 3"/>
    </svg>

    <p class="attribution">-Neil Hartcombe</p>
  </main>
</body>
</html>
```